Brightpath Letterhead

We would like a letterhead for our company. I have uploaded our logo.

Brightpath Ridge Consulting
1450 W Corliss Ave Ste 310
Cedar Hollow, TX 75481
833-517-2906

```html
<!DOCTYPE html>
<html lang="en">
<head>
<meta charset="utf-8">
<title>Brightpath Letterhead</title>
<link href="https://fonts.googleapis.com/css2?family=Jost:wght@400;500&display=swap" rel="stylesheet">
<style>
  :root {
    --teal: #075c6a;
    --mint: #6bc59a;
    --paper: #ffffff;
    --backdrop: #e6e6e6;
  }
  * { margin: 0; padding: 0; box-sizing: border-box; }
  html, body {
    width: 1200px;
    height: 1200px;
    overflow: hidden;
    background: var(--backdrop);
  }
  .letterhead {
    position: absolute;
    left: 133px;
    top: 0;
    width: 934px;
    height: 1200px;
    background: var(--paper);
    overflow: hidden;
  }
  .brand {
    position: absolute;
    left: 68px;
    top: 62px;
    display: flex;
    align-items: center;
    gap: 16px;
  }
  .brand-dot {
    width: 56px;
    height: 56px;
    border-radius: 50%;
    background: var(--teal);
  }
  .brand-name {
    font-family: "Jost", sans-serif;
    font-weight: 500;
    color: var(--teal);
    text-transform: uppercase;
    letter-spacing: 3px;
    line-height: 1.1;
  }
  .brand-name .line-1 { display: block; font-size: 29px; }
  .brand-name .line-2 { display: block; font-size: 23px; }
  .contact {
    position: absolute;
    left: 619px;
    top: 62px;
    height: 63px;
    border-left: 2px solid var(--teal);
    padding-left: 16px;
    font-family: "Jost", sans-serif;
    font-style: normal;
    font-weight: 400;
    font-size: 17px;
    line-height: 23px;
    color: var(--teal);
  }
  .contact-row {
    display: flex;
    align-items: center;
    gap: 6px;
    white-space: nowrap;
  }
  .contact-row .icon { width: 14px; height: 16px; flex: none; }
  .contact-row.indent { padding-left: 20px; }
  .footer-band {
    position: absolute;
    left: 0;
    bottom: 0;
    width: 934px;
    height: 72px;
    background: var(--teal);
  }
  .footer-rule {
    position: absolute;
    left: 0;
    bottom: 84px;
    width: 934px;
    height: 6px;
    background: var(--mint);
  }
</style>
</head>
<body>
  <main class="letterhead">
    <header class="brand">
      <span class="brand-dot"></span>
      <p class="brand-name">
        <span class="line-1">Brightpath Ridge</span>
        <span class="line-2">Consulting</span>
      </p>
    </header>

    <address class="contact">
      <div class="contact-row">
        <svg class="icon" viewBox="0 0 14 18"><path d="M7 0a7 7 0 0 0-7 7c0 5 7 11 7 11s7-6 7-11a7 7 0 0 0-7-7zm0 10a3 3 0 1 1 0-6 3 3 0 0 1 0 6z" fill="var(--mint)"/></svg>
        <span>1450 W Corliss Ave Ste 310</span>
      </div>
      <div class="contact-row indent"><span>Cedar Hollow, TX 75481</span></div>
      <div class="contact-row">
        <svg class="icon" viewBox="0 0 16 16"><path d="M3.5 1.5l2.5 3-1.5 1.8c.8 1.9 2.3 3.4 4.2 4.2L10.5 9l3 2.5-1.2 2.5C7 14 2 9 2 3.7z" fill="none" stroke="var(--mint)" stroke-width="1.5" stroke-linejoin="round"/><path d="M9.5 2.5a4 4 0 0 1 4 4M9.5 0.5a6 6 0 0 1 6 6" fill="none" stroke="var(--mint)" stroke-width="1.3"/></svg>
        <span>833-517-2906</span>
      </div>
    </address>

    <div class="footer-rule"></div>
    <div class="footer-band"></div>
  </main>
</body>
</html>
```